Business Card Design

I would like a new business card design for an accounting firm that specializes in resolving clients tax problems. I want the card to give the impression that we are not your typical stodgy accounting firm, but at the same time we will get the job done.
Industry/Entity Type
Business
Contact Information for Business Card
Marcus T Kelbeck
Certified Public Accountant
27-08 63rd Avenue
Sunnyside, NY 11104
Tel: (718) 555-0143
Fax: (888) 555-0176
e-mail: mtkledger@quillpost.net
website: harborstonefiscalaidgroup.com

```html
<!DOCTYPE html>
<html lang="en">
<head>
<meta charset="utf-8">
<title>Marcus T Kelbeck – Business Card</title>
<link rel="stylesheet" href="https://fonts.googleapis.com/css2?family=Open+Sans:wght@400;600&display=swap">
<style>
  :root {
    --page: #e9e9eb;
    --card-white: #f4f4f5;
    --navy: #1c3d72;
    --wave-grey: #8d9096;
    --gold: #e6b11b;
    --light-text: #ffffff;
    --soft-text: #cfd7e6;
  }
  html, body {
    margin: 0;
    width: 1200px;
    height: 902px;
    overflow: hidden;
    background: var(--page);
    font-family: "Open Sans", Arial, sans-serif;
  }
  .card {
    position: absolute;
    left: 60px;
    top: 142px;
    width: 1080px;
    height: 617px;
    background: var(--card-white);
    box-shadow: 0 10px 30px rgba(0,0,0,0.18);
    overflow: hidden;
  }
  .card-wave {
    position: absolute;
    inset: 0;
    width: 100%;
    height: 100%;
  }
  .brand-name {
    position: absolute;
    left: 0;
    right: 120px;
    top: 78px;
    text-align: center;
    margin: 0;
    font-weight: 600;
    font-size: 46px;
    line-height: 1.2;
    letter-spacing: 6px;
    text-transform: uppercase;
    color: var(--navy);
  }
  .holder {
    position: absolute;
    left: 70px;
    top: 450px;
    color: var(--light-text);
  }
  .holder-name {
    margin: 0;
    font-size: 40px;
    font-weight: 400;
  }
  .holder-title {
    margin: 2px 0 0;
    font-size: 25px;
    color: var(--soft-text);
  }
  .divider {
    position: absolute;
    left: 560px;
    top: 330px;
    width: 2px;
    height: 210px;
    background: var(--light-text);
    opacity: 0.85;
  }
  .contact-list {
    position: absolute;
    left: 588px;
    top: 340px;
    margin: 0;
    padding: 0;
    list-style: none;
    color: var(--light-text);
    font-size: 24px;
  }
  .contact-item {
    display: flex;
    align-items: center;
    gap: 12px;
    height: 46px;
  }
  .contact-icon {
    width: 26px;
    height: 26px;
    flex: none;
  }
</style>
</head>
<body>
  <div class="card">
    <svg class="card-wave" viewBox="0 0 1080 617" preserveAspectRatio="none" aria-hidden="true">
      <path d="M0,392 C260,392 420,372 580,262 C690,186 860,166 1080,166 L1080,617 L0,617 Z" fill="var(--wave-grey)"/>
      <path d="M0,414 C270,414 440,394 600,282 C710,206 870,188 1080,188 L1080,617 L0,617 Z" fill="var(--navy)"/>
    </svg>

    <h1 class="brand-name">Marcus T Kelbeck</h1>

    <div class="holder">
      <p class="holder-name">Marcus T Kelbeck</p>
      <p class="holder-title">Certified Public Accountant</p>
    </div>

    <div class="divider"></div>

    <ul class="contact-list">
      <li class="contact-item">
        <svg class="contact-icon" viewBox="0 0 26 26" aria-label="Telephone">
          <rect width="26" height="26" rx="3" fill="var(--gold)"/>
          <path d="M8 6 l3 0 l1 4 l-2 1.5 a9 9 0 0 0 4.5 4.5 l1.5 -2 l4 1 l0 3 a2 2 0 0 1 -2 2 A13 13 0 0 1 6 8 a2 2 0 0 1 2 -2 z" fill="var(--navy)"/>
        </svg>
        <span>(718) 555-0143</span>
      </li>
      <li class="contact-item">
        <svg class="contact-icon" viewBox="0 0 26 26" aria-label="Fax">
          <rect width="26" height="26" rx="3" fill="var(--gold)"/>
          <rect x="8" y="5" width="10" height="6" fill="none" stroke="var(--navy)" stroke-width="1.6"/>
          <rect x="5" y="11" width="16" height="9" rx="1.5" fill="var(--navy)"/>
          <rect x="8" y="16" width="10" height="5" fill="var(--gold)" stroke="var(--navy)" stroke-width="1.2"/>
        </svg>
        <span>(888) 555-0176</span>
      </li>
      <li class="contact-item">
        <svg class="contact-icon" viewBox="0 0 26 26" aria-label="Email">
          <rect width="26" height="26" rx="3" fill="var(--gold)"/>
          <rect x="5" y="8" width="16" height="11" fill="var(--navy)"/>
          <path d="M5 8 L13 14.5 L21 8" fill="none" stroke="var(--gold)" stroke-width="1.5"/>
        </svg>
        <span>mtkledger@quillpost.net</span>
      </li>
      <li class="contact-item">
        <svg class="contact-icon" viewBox="0 0 26 26" aria-label="Website">
          <rect width="26" height="26" rx="3" fill="var(--gold)"/>
          <circle cx="13" cy="13" r="7.5" fill="none" stroke="var(--navy)" stroke-width="1.6"/>
          <ellipse cx="13" cy="13" rx="3.2" ry="7.5" fill="none" stroke="var(--navy)" stroke-width="1.3"/>
          <line x1="5.5" y1="13" x2="20.5" y2="13" stroke="var(--navy)" stroke-width="1.3"/>
        </svg>
        <span>www.harborstonefiscalaidgroup.com</span>
      </li>
    </ul>
  </div>
</body>
</html>
```